Create Stationary from existing logo(s)

We are looking for some assistance in tidying up the stationary that supports our brand. We are an innovative technology company, generally working with larger corporates. We have previously done a little work on brochures etc, but never really pulled it all together with our stationary.
In particular I am looking for:
1. A4 Letter Template for Letter (Microsoft Word 2007 template format)
2. A4 Template for Reports (Microsoft Word 2007 template format). This should include title page, table of contents, subsequent report pages including styles for tables, headings, and text.
3. Business Card Design - we will need to be able to edit the text, so the card should include sample text for name, title, phone number, mobile number, and email address.
4. Presentation Template (Microsoft Powerpoint 2007 template). See attached powerpoint which we quite like, but isn't really a template, and we have don't really use any consistent styles in it. The Powerpoint template needs to have a cover / title page, section break pages, and pages that may contain bullet point text, pictures, or a combination of bullet point text and pictures. We do like our current presentation, which gives some indication of our thinking.
I am attaching a brochure and the powerpoint presentation to give some indication of current materials. We are happy with the main concepts behind the brochure, and would not really be looking to change the key concepts unless you have a compelling reason. We do like the use of this secondary logo in the stationary related items
I have uploaded an eps file of the logo.

```html
<!DOCTYPE html>
<html lang="en">
<head>
<meta charset="utf-8">
<title>Novara Systems – Presentation Slide</title>
<link rel="stylesheet" href="https://fonts.googleapis.com/css2?family=Arimo:wght@400&display=swap">
<style>
  :root {
    --brand-blue: #1d4f8a;
    --brand-orange: #f0871e;
    --peach: #f9c9a1;
    --text-dark: #4a4a4a;
    --text-mid: #555a60;
    --frame-grey: #c9c9c9;
    --wave-light: #d6eaf8;
    --wave-mid: #7cbce8;
    --wave-deep: #2b7fc4;
    --paper: #ffffff;
  }
  * { margin: 0; padding: 0; box-sizing: border-box; }
  html, body { width: 1200px; height: 845px; overflow: hidden; background: var(--paper); }
  body { font-family: "Arimo", Arial, sans-serif; }

  .slide { position: relative; width: 1200px; height: 845px; overflow: hidden; background: var(--paper); }

  .corner-arc { position: absolute; left: 0; top: 0; }

  .slide-title {
    position: absolute; left: 114px; top: 76px;
    font-size: 42px; font-weight: 400; color: var(--brand-blue);
    letter-spacing: 0.5px;
  }

  .brand {
    position: absolute; right: 54px; top: 66px;
    display: flex; align-items: center; gap: 12px;
  }
  .brand-mark { width: 34px; height: 34px; background: var(--brand-blue); }
  .brand-name { font-size: 30px; font-weight: 400; color: var(--brand-blue); }

  .intro { position: absolute; left: 241px; top: 234px; width: 342px; }
  .intro-heading { font-size: 24px; font-weight: 400; color: var(--text-mid); margin-bottom: 16px; }
  .intro-body { font-size: 14.2px; line-height: 17.3px; color: var(--text-dark); hyphens: auto; }

  .feature-box {
    position: absolute; left: 639px; top: 239px; width: 341px; height: 315px;
    border: 1.5px solid var(--frame-grey); border-radius: 14px;
  }
  .feature-list { list-style: none; position: absolute; left: 30px; top: 28px; }
  .feature-list li {
    display: flex; align-items: center; gap: 14px;
    height: 48.5px; font-size: 18.5px; color: var(--text-mid);
  }
  .feature-list svg { flex: none; }

  .footer-decor {
    position: absolute; left: 0; bottom: 0; width: 1200px; height: 175px;
    background:
      linear-gradient(to bottom, rgba(255,255,255,1) 0%, rgba(255,255,255,0) 45%),
      linear-gradient(to right, var(--peach) 0%, var(--wave-mid) 30%, var(--wave-light) 50%, var(--wave-mid) 75%, var(--wave-deep) 100%);
  }
</style>
</head>
<body>
<main class="slide">
  <svg class="corner-arc" width="140" height="80" viewBox="0 0 140 80" aria-hidden="true">
    <path d="M0 0 H138 C80 8 30 35 0 80 Z" fill="var(--brand-blue)"/>
  </svg>

  <h1 class="slide-title">YOUR TITTLE HERE</h1>

  <div class="brand">
    <span class="brand-mark"></span>
    <span class="brand-name">Novara Systems</span>
  </div>

  <section class="intro">
    <h2 class="intro-heading">YOUR SUBTITTLE</h2>
    <p class="intro-body">Lorem Ipsum is simply dummy text of the printing and typesetting industry. Lorem Ipsum has been the industry's standard dummy text ever since the 1500s, when an unknown printer took a galley of type and scrambled it to make a type specimen book. It has survived not only five centuries, but also the leap into electronic type-setting, remaining essentially unchanged. It was popularised in the 1960s with the release of Typeset sheets containing Lorem Ipsum passages, and more recently with desktop publishing software like Folio Layout including versions of Lorem Ipsum.</p>
  </section>

  <aside class="feature-box">
    <ul class="feature-list">
      <li><svg width="12" height="12" viewBox="0 0 12 12" aria-hidden="true"><path d="M3 1 L9 6 L3 11" fill="none" stroke="var(--brand-orange)" stroke-width="2.4"/></svg>Orbit Desk</li>
      <li><svg width="12" height="12" viewBox="0 0 12 12" aria-hidden="true"><path d="M3 1 L9 6 L3 11" fill="none" stroke="var(--brand-orange)" stroke-width="2.4"/></svg>Summit OS</li>
      <li><svg width="12" height="12" viewBox="0 0 12 12" aria-hidden="true"><path d="M3 1 L9 6 L3 11" fill="none" stroke="var(--brand-orange)" stroke-width="2.4"/></svg>Kernel One</li>
      <li><svg width="12" height="12" viewBox="0 0 12 12" aria-hidden="true"><path d="M3 1 L9 6 L3 11" fill="none" stroke="var(--brand-orange)" stroke-width="2.4"/></svg>Summit OS</li>
      <li><svg width="12" height="12" viewBox="0 0 12 12" aria-hidden="true"><path d="M3 1 L9 6 L3 11" fill="none" stroke="var(--brand-orange)" stroke-width="2.4"/></svg>Orbit Classic</li>
    </ul>
  </aside>

  <div class="footer-decor" role="img" aria-label="Decorative footer: peach circles and a flowing fine-line blue wave pattern across the foot of the slide"></div>
</main>
</body>
</html>
```